Dialysis Brochure

12 pages booklet, horizontal, 9 inches width x 6 inches high , luxury look
Updates

Landscape booklet 9 x 6

Need extra days to review

Target Market(s)

General public

Industry/Entity Type

Health Care

Colors

Designer to choose colors to be used in the design.

Requirements
Nice to have
• foil effect or similar

```html
<!DOCTYPE html>
<html lang="en">
<head>
<meta charset="utf-8">
<title>Dialysis Brochure – Spread 8 / 5</title>
<link rel="stylesheet" href="https://fonts.googleapis.com/css2?family=Montserrat:ital,wght@0,800;1,500&family=Questrial&family=Tinos:wght@700&display=swap">
<style>
  :root {
    --navy: #0a3a8c;
    --blue: #0062b2;
    --orange: #ee7d1e;
    --pink: #e5097f;
    --ink: #1a1a1a;
    --paper: #ffffff;
  }
  * { margin: 0; padding: 0; box-sizing: border-box; }
  html, body { width: 1200px; height: 849px; overflow: hidden; background: var(--paper); }
  .spread { position: relative; width: 1200px; height: 849px; overflow: hidden; background: var(--paper); font-family: "Questrial", sans-serif; color: var(--ink); }
  .layer { position: absolute; left: 0; top: 0; }

  .fact-band { position: absolute; left: 0; width: 600px; height: 21px; background: var(--navy); }
  .fact-title { position: absolute; left: 84px; font-family: "Montserrat", sans-serif; font-weight: 800; font-size: 16px; color: #fff; line-height: 21px; }
  .fact-text { position: absolute; left: 84px; width: 447px; font-size: 17.8px; line-height: 20.6px; text-align: justify; }

  .page-title { position: absolute; left: 891px; top: 458px; font-family: "Montserrat", sans-serif; font-style: italic; font-weight: 500; font-size: 43px; line-height: 43px; color: #fff; letter-spacing: -0.5px; }

  .service-rule { position: absolute; left: 676px; top: 627px; width: 2px; height: 114px; background: var(--orange); }
  .service-rule::before { content: ""; position: absolute; left: -3px; top: 20px; width: 1px; height: 80px; background: #bbb; }
  .service-list { position: absolute; left: 686px; top: 642px; list-style: none; font-size: 17.6px; line-height: 17px; }
  .service-list li { margin-bottom: 10px; }
  .service-list li:last-child { margin-bottom: 0; }

  .folio { position: absolute; top: 781px; height: 19px; }
  .folio-bar { position: absolute; top: 0; height: 19px; background: var(--pink); }
  .folio-num { position: absolute; top: 0; width: 24px; height: 19px; background: #000; color: #fff; font-family: "Tinos", serif; font-weight: 700; font-size: 15px; line-height: 19px; text-align: center; }
</style>
</head>
<body>
<main class="spread">

  <!-- left page: facility photo with warm diagonal -->
  <svg class="layer" width="600" height="849" viewBox="0 0 600 849" role="img" aria-label="Photo of the bright marble reception lobby with a white front desk">
    <defs>
      <linearGradient id="lobbyTone" x1="0" y1="0" x2="1" y2="1">
        <stop offset="0" stop-color="#f4f5f7"/>
        <stop offset="0.35" stop-color="#dcdfe3"/>
        <stop offset="0.6" stop-color="#c9cdd2"/>
        <stop offset="0.8" stop-color="#a9764f"/>
        <stop offset="1" stop-color="#e9e9ea"/>
      </linearGradient>
      <linearGradient id="lobbyWarm" x1="0" y1="0" x2="1" y2="1">
        <stop offset="0" stop-color="#f3c59e"/>
        <stop offset="0.7" stop-color="#efb88a"/>
        <stop offset="1" stop-color="#c98e60"/>
      </linearGradient>
    </defs>
    <rect x="0" y="350" width="600" height="499" fill="url(#lobbyTone)"/>
    <polygon points="600,457 600,849 0,849" fill="url(#lobbyWarm)" opacity="0.9"/>
  </svg>

  <div class="fact-band" style="top:56px"></div>
  <h2 class="fact-title" style="top:56px">Patient Survival Rate</h2>
  <p class="fact-text" style="top:79px">HRKC had the Lowest Mortality Rate (higher survival) in New York State for 2011-2017 years – 11.7 (per 100 patients)</p>

  <div class="fact-band" style="top:160px"></div>
  <h2 class="fact-title" style="top:160px">Medcover Rating:</h2>
  <p class="fact-text" style="top:182px">HRKC received 5-Star rating 9 times out of the last 10 years. Only 15% of Dialysis Centers in the United States receive 5-Star rating in any particular year</p>

  <div class="fact-band" style="top:263px"></div>
  <h2 class="fact-title" style="top:263px">Patient Safety Program:</h2>
  <p class="fact-text" style="top:285px">&nbsp;5-Diamond Award – 2016, 2017, 2018. Every single year starting 2016 when this program was established</p>

  <div class="folio" style="left:0">
    <span class="folio-bar" style="left:0;width:45px"></span>
    <span class="folio-num" style="left:50px">8</span>
  </div>

  <!-- right page: treatment photo and angled shapes -->
  <svg class="layer" style="left:600px" width="600" height="849" viewBox="0 0 600 849">
    <defs>
      <linearGradient id="clinicTone" x1="0" y1="0" x2="1" y2="1">
        <stop offset="0" stop-color="#eef0f2"/>
        <stop offset="0.3" stop-color="#d6dade"/>
        <stop offset="0.5" stop-color="#2f6fc4"/>
        <stop offset="0.65" stop-color="#9b9b9e"/>
        <stop offset="0.85" stop-color="#e6e8ea"/>
        <stop offset="1" stop-color="#c8a27c"/>
      </linearGradient>
    </defs>
    <polygon role="img" aria-label="Photo of a nurse and doctor attending a patient in a dialysis chair" points="0,0 600,0 600,306 270,442 0,395" fill="url(#clinicTone)"/>
    <polygon points="0,398 217,453 0,543" fill="var(--orange)"/>
    <polygon points="600,313 90,523 600,648" fill="var(--blue)"/>
  </svg>

  <h1 class="page-title">DOCTOR'S<br>SERVICES</h1>

  <div class="service-rule"></div>
  <ul class="service-list">
    <li>Full-time Nephrology staff physician on premises</li>
    <li>11 Board Certified Nephrologists</li>
    <li>or YOU MAY KEEP YOUR CURRENT NEPHROLOGIST<br>when you transfer to our Center</li>
  </ul>

  <div class="folio" style="left:1126px">
    <span class="folio-num" style="left:0">5</span>
    <span class="folio-bar" style="left:29px;width:45px"></span>
  </div>

</main>
</body>
</html>
```